business cards

we want our logos on the back
the information on it are on the design I've uploaded
come up with whatever you think is best, we want something professional, sophisticated and sleek.

```html
<!DOCTYPE html>
<html lang="en">
<head>
<meta charset="utf-8">
<title>Keystone Health and Performance – Business Cards</title>
<link href="https://fonts.googleapis.com/css2?family=Montserrat:wght@400;500&family=Roboto:wght@400;500&display=swap" rel="stylesheet">
<style>
  :root {
    --stage: #222224;
    --brand-green: #54b848;
    --card-dark: #232326;
    --ink-light: #ffffff;
    --ink-soft: #e8e8e8;
    --card-radius: 26px;
  }
  * { margin: 0; padding: 0; box-sizing: border-box; }
  html, body { width: 1200px; height: 711px; overflow: hidden; background: var(--stage); }
  .stage {
    position: relative; width: 1200px; height: 711px;
    display: flex; align-items: center; justify-content: center; gap: 44px;
  }
  .card {
    position: relative; width: 520px; height: 312px;
    border-radius: var(--card-radius); overflow: hidden;
    box-shadow: 0 18px 40px rgba(0,0,0,.55);
  }
  /* Front */
  .card--front { background: var(--brand-green); }
  .front-brand {
    position: absolute; left: 50%; top: 50%; transform: translate(-50%, -50%);
    text-align: center; color: var(--ink-light);
  }
  .brand-name {
    font-family: "Montserrat", sans-serif; font-weight: 400;
    letter-spacing: .32em; text-transform: uppercase; white-space: nowrap;
    display: flex; align-items: center; gap: 14px;
  }
  .brand-mark { width: 14px; height: 14px; background: currentColor; flex: none; }
  .front-brand .brand-name { font-size: 26px; }
  .brand-sub {
    font-family: "Montserrat", sans-serif; font-weight: 400;
    letter-spacing: .42em; text-transform: uppercase; font-size: 11px;
    margin-top: 8px; padding-bottom: 6px; border-bottom: 1px solid currentColor;
    white-space: nowrap;
  }
  .brand-services {
    font-family: "Montserrat", sans-serif; font-size: 8.5px; letter-spacing: .08em;
    text-transform: uppercase; margin-top: 6px; white-space: nowrap;
  }
  /* Back */
  .card--back {
    background: var(--card-dark);
    border-bottom: 4px solid var(--brand-green);
  }
  .back-brand {
    position: absolute; left: 30px; top: 18px;
    writing-mode: vertical-rl; color: var(--ink-light);
  }
  .back-brand .brand-name { font-size: 20px; letter-spacing: .28em; gap: 12px; }
  .back-brand .brand-mark { width: 11px; height: 11px; background: var(--brand-green); }
  .back-brand .brand-sub {
    font-size: 9px; margin-top: 0; margin-right: 6px; padding-bottom: 0;
    padding-left: 5px; border-bottom: 0; border-left: 1px solid var(--ink-light);
  }
  .back-brand .brand-services {
    font-size: 6.5px; letter-spacing: .02em; margin-top: 0; margin-right: 4px;
    color: var(--brand-green);
  }
  .contact {
    position: absolute; right: 30px; top: 34px; text-align: right;
    font-family: "Roboto", sans-serif; color: var(--ink-soft);
  }
  .contact-name { font-size: 26px; color: var(--brand-green); font-weight: 400; line-height: 1.1; }
  .contact-name strong { font-weight: 500; }
  .contact-role { font-size: 11.5px; line-height: 1.35; margin-top: 4px; }
  .contact-details { list-style: none; margin-top: 22px; font-size: 12px; line-height: 1.55; }
  .contact-details li { display: flex; justify-content: flex-end; align-items: center; gap: 8px; }
  .contact-details svg { width: 12px; height: 12px; fill: var(--brand-green); flex: none; }
  .contact-details .no-icon { padding-right: 20px; }
  .contact-email {
    position: absolute; right: 30px; bottom: 26px;
    font-family: "Roboto", sans-serif; font-size: 12px; color: var(--ink-soft);
  }
</style>
</head>
<body>
<main class="stage">
  <section class="card card--front" aria-label="Card front">
    <div class="front-brand">
      <div class="brand-name"><span class="brand-mark"></span>Keystone</div>
      <div class="brand-sub">Health and Performance</div>
      <div class="brand-services">Physio · S&amp;C · Coaching · Personal Training · Rehab · Recovery</div>
    </div>
  </section>

  <section class="card card--back" aria-label="Card back">
    <div class="back-brand">
      <div class="brand-name"><span class="brand-mark"></span>Keystone</div>
      <div class="brand-sub">Health and Performance</div>
      <div class="brand-services">Physio · S&amp;C · Coaching · Personal Training · Rehab · Recovery</div>
    </div>

    <div class="contact">
      <h1 class="contact-name"><strong>Daniel</strong> Moretti</h1>
      <p class="contact-role">DIRECTOR<br>SENIOR PHYSIOTHERAPIST<br>BHlthSc, MPhysioPrac, MExSc(S&amp;C)<br>ASCA Level 2</p>
      <ul class="contact-details">
        <li class="no-icon">17 Larkin Rd, Westfield Park</li>
        <li>03 9000 1482
          <svg viewBox="0 0 24 24" aria-hidden="true"><path d="M6.6 10.8a15 15 0 0 0 6.6 6.6l2.2-2.2c.3-.3.7-.4 1-.2 1.1.4 2.3.6 3.6.6.6 0 1 .4 1 1V20c0 .6-.4 1-1 1A17 17 0 0 1 3 4c0-.6.4-1 1-1h3.5c.6 0 1 .4 1 1 0 1.3.2 2.5.6 3.6.1.3 0 .7-.2 1z"/></svg>
        </li>
        <li>03 9000 3617
          <svg viewBox="0 0 24 24" aria-hidden="true"><path d="M6 2h9v6H6zM4 9h16a2 2 0 0 1 2 2v10H2V11a2 2 0 0 1 2-2zm3 4v2h2v-2zm4 0v2h2v-2zm4 0v2h2v-2zm-8 4v2h2v-2zm4 0v2h2v-2zm4 0v2h2v-2z"/></svg>
        </li>
      </ul>
    </div>
    <p class="contact-email">dan@keystonehealthandperformance.com.au</p>
  </section>
</main>
</body>
</html>
```